Flyer for Lawnmowing and gardening business

We are a lawn mowing and gardening business needing a flyer designed listing our services and business info.
The flyer should include all business information and contact details as below.

Lawn mowing
Gardening
Green waste removal
Pruning
Weeding
Vegetable Garden Creation

Phone number:0481657240

As well as the logo provided

Target Market(s)

Local people wanting someone to care for their garden.

Industry/Entity Type

Gardener

Font styles to use
Serif

Requirements
Must have
• Business Logo
• All business info and services provided. EG
• Lawn mowing
• Gardening
• Green waste removal
• Pruning
• Weeding
• Vegetable Garden Creation
• Phone number:0481657240
Nice to have
• Earthy tones, clean and simple flyer design

```html
<!DOCTYPE html>
<html lang="en">
<head>
<meta charset="utf-8">
<title>Fernvale Green – Lawn Mowing &amp; Garden Care</title>
<link rel="stylesheet" href="https://fonts.googleapis.com/css2?family=Cinzel:wght@400;600&display=swap">
<style>
  :root {
    --paper: #ffffff;
    --bark: #4a3326;
    --leaf: #4f7a2b;
    --leaf-text: #56722f;
    --sky: #9cc3e6;
    --lawn: #5f8f2e;
    --lawn-deep: #3c6420;
  }
  * { margin: 0; padding: 0; box-sizing: border-box; }
  html, body { width: 1200px; height: 2544px; overflow: hidden; background: var(--paper); }
  .flyer {
    position: relative;
    width: 1200px;
    height: 2544px;
    background: var(--paper);
    font-family: "Cinzel", "Times New Roman", serif;
    overflow: hidden;
  }
  .brand {
    position: absolute;
    top: 150px;
    left: 0;
    width: 1200px;
    text-align: center;
  }
  .brand-mark {
    display: block;
    width: 200px;
    height: 200px;
    margin: 0 auto 60px;
    border-radius: 50%;
    background: var(--leaf);
  }
  .brand-name {
    font-size: 104px;
    font-weight: 400;
    color: var(--bark);
    letter-spacing: 2px;
    line-height: 1;
  }
  .brand-tagline {
    margin-top: 18px;
    font-size: 50px;
    color: var(--leaf);
    letter-spacing: 1px;
    line-height: 1;
  }
  .phone-band {
    position: absolute;
    top: 748px;
    left: 0;
    width: 1200px;
    height: 112px;
    background: var(--leaf);
    display: flex;
    align-items: center;
    justify-content: center;
  }
  .phone-number {
    color: var(--paper);
    font-size: 70px;
    letter-spacing: 8px;
    font-weight: 400;
  }
  .service {
    position: absolute;
    font-size: 46px;
    line-height: 1.05;
    color: var(--leaf-text);
    letter-spacing: 2px;
    text-align: center;
  }
  .service-icon {
    position: absolute;
    background: var(--bark);
    border-radius: 18px;
  }
  .garden-photo {
    position: absolute;
    left: 0;
    top: 1720px;
    width: 1200px;
    height: 824px;
    background:
      linear-gradient(to bottom, var(--paper) 0%, rgba(255,255,255,0) 22%),
      linear-gradient(to bottom, var(--sky) 0%, #b9d3ad 35%, var(--lawn) 65%, var(--lawn-deep) 100%);
  }
</style>
</head>
<body>
<main class="flyer">
  <header class="brand">
    <span class="brand-mark" aria-hidden="true"></span>
    <h1 class="brand-name">Fernvale Green</h1>
    <p class="brand-tagline">Lawn Mowing &amp; Garden Care</p>
  </header>

  <section class="phone-band">
    <p class="phone-number">0481 657 240</p>
  </section>

  <section class="services">
    <div class="service-icon" role="img" aria-label="Lawn mower icon" style="left:80px; top:980px; width:180px; height:140px;"></div>
    <p class="service" style="left:370px; top:1020px;">Lawn<br>Mowing</p>

    <div class="service-icon" role="img" aria-label="Watering can icon" style="left:940px; top:1040px; width:160px; height:160px;"></div>
    <p class="service" style="left:580px; top:1150px;">Gardening</p>

    <div class="service-icon" role="img" aria-label="Pruning secateurs icon" style="left:80px; top:1220px; width:170px; height:120px;"></div>
    <p class="service" style="left:352px; top:1235px;">Pruning</p>

    <div class="service-icon" role="img" aria-label="Trowel and fork icon" style="left:948px; top:1280px; width:140px; height:140px;"></div>
    <p class="service" style="left:580px; top:1320px;">Weeding</p>

    <div class="service-icon" role="img" aria-label="Seed packet icon" style="left:88px; top:1460px; width:160px; height:160px;"></div>
    <p class="service" style="left:280px; top:1405px;">Vegetable<br>Garden<br>Creation</p>

    <div class="service-icon" role="img" aria-label="Wheelbarrow icon" style="left:920px; top:1520px; width:200px; height:140px;"></div>
    <p class="service" style="left:580px; top:1570px;">Green<br>Waste<br>Removal</p>
  </section>

  <div class="garden-photo" role="img" aria-label="Photo of a lawn mower on freshly cut grass with trees and blue sky behind"></div>
</main>
</body>
</html>
```